Visitenkarten-Design für Catering/ Liefertouren
Vielen Dank für die professionelle Zusammenarbeit. Änderungen wurden schnell und treffend umgesetzt. Wir sind mit dem Ergebnis sehr zufrieden.
Zielgruppe
Catering/ Liefertouren für hochwertige selbstgemachte Quiches/ französische Tartes, Suppen, Currys
Aufgabenstellung
2 Visitenkarten im Format DIN6 (21x10,5) lang die sich auf der 1. (Bild) Seite unterscheiden aber mit identischer 2. Seite.
Karte 'Quiche' 1. Seite:
'Quiche '
Quiche Passion - depuis 2003
Quiches, Soups, Currys,
Catering, Abholung, Liefertouren
www.Kovendo.de,
info@kovendo.de
Karte 'Soups' 1. Seite:
'KovendoChicken, KovendoTofu'
2. Seite (für beide Karten identisch)
Seite soll eine Art Vorlage sein und besteht lediglich aus einer gestalterischen 'Umrahmung' und unserem Logo am unteren Seitenrand. Der Durchmesser des Logos soll max. 15% der gesamten Seitenlänge betragen.
Seite wird von uns mit Angeboten/ Aktionen bedruckt in kleiner Stückzahl nachträglich bedruckt.
1. Seiten (Quer- oder Hochformat je nach Bild möglich).
2. Seite im Hochformat.
Keine Vorgaben bzgl. Schrifttyp.

```html
<!DOCTYPE html>
<html lang="de">
<head>
<meta charset="utf-8">
<title>Kovendo – Quiche</title>
<link href="https://fonts.googleapis.com/css2?family=Allura&family=Arimo:wght@400&display=swap" rel="stylesheet">
<style>
  :root {
    --slate-dark: #2b2f33;
    --slate-mid: #4a5057;
    --tomato: #b4452a;
    --tomato-deep: #7e2a18;
    --pepper-red: #c7261c;
    --pepper-yellow: #e8b51c;
    --herb-green: #5f8a3a;
    --brand-brown: #4a2520;
    --tab-white: rgba(255, 255, 255, 0.72);
    --text-white: #ffffff;
  }
  * { margin: 0; padding: 0; box-sizing: border-box; }
  html, body { width: 850px; height: 1200px; overflow: hidden; background: var(--slate-dark); }
  .card {
    position: relative;
    width: 850px;
    height: 1200px;
    overflow: hidden;
    font-family: "Arimo", Arial, sans-serif;
    color: var(--text-white);
  }
  .food-photo {
    position: absolute;
    inset: 0;
    background:
      radial-gradient(circle at 46% 64%, var(--tomato) 0, var(--tomato-deep) 22%, transparent 34%),
      radial-gradient(circle at 82% 12%, var(--pepper-yellow) 0, transparent 14%),
      radial-gradient(circle at 55% 22%, var(--pepper-red) 0, transparent 14%),
      radial-gradient(circle at 92% 40%, var(--herb-green) 0, transparent 16%),
      radial-gradient(circle at 16% 30%, #8d9196 0, transparent 22%),
      radial-gradient(circle at 40% 1150px, #d1652f 0, transparent 14%),
      linear-gradient(160deg, var(--slate-mid), var(--slate-dark));
  }
  .brand-tab {
    position: absolute;
    left: 335px;
    top: 0;
    width: 238px;
    height: 287px;
    background: var(--tab-white);
    border-radius: 0 0 30px 30px;
    display: flex;
    flex-direction: column;
    align-items: center;
    justify-content: center;
    gap: 18px;
    padding-top: 20px;
  }
  .brand-dot {
    width: 26px;
    height: 26px;
    border-radius: 50%;
    background: var(--brand-brown);
  }
  .brand-name {
    font-family: "Arimo", Arial, sans-serif;
    font-size: 40px;
    color: var(--brand-brown);
  }
  .title-script {
    position: absolute;
    left: 52px;
    top: 392px;
    font-family: "Allura", cursive;
    font-weight: 400;
    font-size: 292px;
    line-height: 1;
    text-shadow: 0 2px 8px rgba(0,0,0,0.35);
  }
  .tagline {
    position: absolute;
    right: 88px;
    top: 655px;
    text-align: right;
    font-size: 41px;
    line-height: 52px;
    text-shadow: 0 2px 6px rgba(0,0,0,0.45);
  }
  .services {
    position: absolute;
    left: 0;
    width: 850px;
    top: 838px;
    text-align: center;
    font-size: 38px;
    line-height: 52px;
    text-shadow: 0 2px 6px rgba(0,0,0,0.45);
  }
  .contact {
    position: absolute;
    right: 22px;
    top: 1052px;
    text-align: right;
    font-style: normal;
    font-size: 25px;
    line-height: 40px;
    text-shadow: 0 2px 6px rgba(0,0,0,0.5);
  }
</style>
</head>
<body>
  <main class="card">
    <div class="food-photo" role="img" aria-label="Foto: Schmortopf mit Tomateneintopf und Quiche-Stücken, umgeben von Paprika, Ingwer, Knoblauch, Zwiebel, Kräutern und Gewürzen auf dunklem Schiefer"></div>

    <div class="brand-tab">
      <span class="brand-dot"></span>
      <span class="brand-name">Kovendo</span>
    </div>

    <h1 class="title-script">Quiche</h1>

    <p class="tagline">Quiche Passion<br>depuis 2003</p>

    <p class="services">Quiches, Soups, Currys,<br>Catering, Abholung, Liefertouren</p>

    <address class="contact">
      www.kovendo.de<br>
      info@kovendo.de<br>
      +49 (0) 89-6120 4857
    </address>
  </main>
</body>
</html>
```